New singe page website for our software development company

We need a single webpage that includes information about our company, contact details and a job posting. It should scroll vertically with some cool animations and parallax scrolling effects.

We are a software development consulting company that writes custom software for our customers. The webpage should have graphics and illustrations that illustrate this.

Find our logo attached, it can be modified as needed.

Thanks for all the design. When looking through the various design it's clear to us, that car related images does not look right.

We got to have software design/engineering images instead.

Our unique selling points are:

• Custom software development
• Project Managment
• Industry Services
We want these displayed with some text and icons. The icons should either have the red/brown colour from our logo, or a colour that matches the design

Software

```html
<!DOCTYPE html>
<html lang="en">
<head>
<meta charset="utf-8">
<title>Norvale Consult — Software Development Consulting</title>
<link href="https://fonts.googleapis.com/css2?family=Montserrat:wght@700&family=Open+Sans:wght@400;600;700;800&display=swap" rel="stylesheet">
<style>
:root{
  --brown:#5a1606;
  --brown-dark:#4a1204;
  --ink:#1f1f1f;
  --text:#6f6f6f;
  --grey-bg:#f3f3f3;
  --white:#ffffff;
  --black:#111111;
  --line:#d8d8d8;
  --footer:#2d2f34;
  --blue:#1a8fd8;
  --olive:#cfc54a;
}
*{box-sizing:border-box;margin:0;padding:0}
html,body{width:1200px;height:2731px;overflow:hidden}
body{position:relative;font-family:"Open Sans",Arial,sans-serif;color:var(--ink);background:var(--white)}
.abs{position:absolute}

/* header */
.site-header{position:absolute;left:0;top:0;width:1200px;height:102px;background:var(--white)}
.brand{position:absolute;left:92px;top:32px;display:flex;align-items:center;gap:10px}
.brand-mark{width:14px;height:14px;background:var(--brown)}
.brand-name{font-family:"Open Sans",Arial,sans-serif;font-weight:700;font-size:27px;color:var(--brown);letter-spacing:.2px}
.social-top{position:absolute;left:868px;top:42px;display:flex;gap:22px}
.social-top span{width:16px;height:16px;border-radius:50%;border:2px solid #8c8c8c}
.plus-box{position:absolute;background:var(--black);display:flex;align-items:center;justify-content:center}

/* hero */
.hero{position:absolute;left:0;top:102px;width:1200px;height:685px;
  background:linear-gradient(180deg,#c9c4bd 0%,#b9b2a8 35%,#8f8678 70%,#6b5e4c 100%)}
.hero-photo{position:absolute;inset:0;
  background:radial-gradient(ellipse 120px 420px at 600px 260px,rgba(120,112,102,.45),transparent 70%),
             linear-gradient(180deg,transparent 55%,rgba(70,58,44,.45) 100%)}
.nav{position:absolute;left:0;top:186px;width:1200px}
.nav-item{position:absolute;width:131px;height:131px;border-radius:50%;background:var(--white);
  display:flex;flex-direction:column;align-items:center;justify-content:center;gap:8px;
  font-size:12px;font-weight:600;color:#2a2a2a;letter-spacing:.3px}
.hero-title{position:absolute;left:0;top:343px;width:1200px;text-align:center;
  font-family:"Montserrat",Arial,sans-serif;font-weight:700;font-size:36px;color:var(--brown)}
.hero-lead{position:absolute;left:300px;top:398px;width:600px;text-align:center;font-size:15px;line-height:22px;color:#222}
.hero-down{position:absolute;left:566px;top:479px;width:66px;height:66px;border-radius:50%;
  background:#2b2b2b;border:2px solid #e8e8e8;display:flex;align-items:center;justify-content:center}

/* sections */
.section{position:absolute;left:0;width:1200px}
.services{top:787px;height:546px;background:var(--grey-bg)}
.about{top:1333px;height:533px;background:var(--white);border-bottom:3px solid var(--line)}
.contact{top:1869px;height:699px;background:var(--grey-bg)}
.section-title{position:absolute;left:0;width:1200px;text-align:center;font-weight:700;font-size:37px;color:var(--ink)}
.section-title::before,.section-title::after{content:"";display:inline-block;width:8px;height:8px;border-radius:50%;
  background:#c4c4c4;vertical-align:middle;margin:0 28px}
.section-sub{position:absolute;left:0;width:1200px;text-align:center;font-size:13px;color:#555}

.card{position:absolute;top:233px;width:283px;height:227px;background:var(--white);border:1px solid #e6e6e6;text-align:center}
.card.active{background:var(--brown);border-color:var(--brown)}
.card-icon{position:absolute;left:106px;top:-33px;width:70px;height:70px;border-radius:50%;background:#2b2b2b;
  display:flex;align-items:center;justify-content:center}
.card.active .card-icon{background:var(--white)}
.card h3{position:absolute;left:0;top:60px;width:100%;font-size:15px;font-weight:400;color:#222;letter-spacing:.2px}
.card.active h3{color:var(--white)}
.card p{position:absolute;left:30px;top:96px;width:223px;font-size:12.5px;line-height:16px;color:var(--text);height:80px;overflow:hidden}
.card.active p{color:#f2e6e2}
.card .more{position:absolute;left:0;top:203px;width:100%;font-size:11.5px;color:#222;text-decoration:underline}
.card.active .more{top:198px;color:var(--white)}

.about-photo{position:absolute;left:102px;top:180px;width:519px;height:262px;
  background:linear-gradient(120deg,#d9dde2 0%,#a8a49e 40%,#3a3a3e 70%,#c9ccd0 100%);
  box-shadow:0 14px 18px -10px rgba(0,0,0,.35)}
.about-text{position:absolute;left:650px;top:180px;width:390px;font-size:13.4px;line-height:19.8px;color:#7a7a7a}
.about-more{position:absolute;left:650px;top:414px;font-size:13px;color:var(--brown);text-decoration:underline}

.info-row{position:absolute;left:110px;display:flex;gap:18px;font-size:14px;line-height:22px;color:#333}
.info-row .ico{width:36px;display:flex;justify-content:center;padding-top:3px}
.info-row.web{color:var(--brown)}

.field{position:absolute;background:var(--white);border:1px solid #dcdcdc;font-size:12px;font-weight:600;color:#555;padding:9px 14px}
.send-btn{position:absolute;left:921px;top:291px;width:113px;height:30px;background:var(--blue);color:var(--white);
  font-size:11.5px;font-weight:700;display:flex;align-items:center;justify-content:center}

.newsletter{position:absolute;left:126px;top:356px;width:402px;height:157px;background:var(--brown-dark);border-radius:3px}
.newsletter h4{position:absolute;left:14px;top:16px;font-size:18px;font-weight:600;color:var(--white)}
.newsletter p{position:absolute;left:14px;top:60px;font-size:12px;color:#f3e9e5}
.news-input{position:absolute;left:14px;top:91px;width:286px;height:37px;background:var(--white);border-radius:2px;
  display:flex;align-items:center;gap:10px;padding-left:12px;font-size:12px;color:#333}
.news-go{position:absolute;left:315px;top:91px;width:60px;height:37px;background:var(--olive);border-radius:2px;
  display:flex;align-items:center;justify-content:center;font-weight:700;font-size:17px;color:#3a3a1a}
.map{position:absolute;left:612px;top:356px;width:428px;height:292px;border:2px solid #cfcfcf;
  background:linear-gradient(135deg,#ecebe8,#e2e1dc)}

.site-footer{position:absolute;left:0;top:2568px;width:1200px;height:163px;background:var(--footer)}
.footer-social{position:absolute;left:0;top:28px;width:1200px;display:flex;justify-content:center;gap:26px}
.footer-social span{width:30px;height:30px;border-radius:50%;border:2.5px solid #f2f2f2}
.footer-links{position:absolute;left:0;top:73px;width:1200px;text-align:center;font-size:13px;color:#eee;word-spacing:2px}
.footer-links i{font-style:normal;margin:0 18px}
.footer-up{position:absolute;left:580px;top:109px;width:40px;height:40px;border-radius:50%;border:2px solid #eee;
  display:flex;align-items:center;justify-content:center}
</style>
</head>
<body>

<header class="site-header">
  <div class="brand"><span class="brand-mark"></span><span class="brand-name">Norvale Consult</span></div>
  <div class="social-top"><span></span><span></span><span></span><span></span></div>
  <div class="plus-box" style="left:1036px;top:0;width:75px;height:102px">
    <svg width="24" height="24" viewBox="0 0 24 24"><path d="M12 2v20M2 12h20" stroke="#fff" stroke-width="2"/></svg>
  </div>
</header>

<section class="hero">
  <div class="hero-photo" role="img" aria-label="Blurred photo of a city skyline with a tall tower"></div>
  <nav class="nav">
    <div class="nav-item" style="left:227px">
      <svg width="22" height="20" viewBox="0 0 22 20"><rect x="3" y="2" width="16" height="16" fill="none" stroke="#222" stroke-width="2"/><rect x="6" y="9" width="5" height="9" fill="#222"/></svg>HOME</div>
    <div class="nav-item" style="left:377px">
      <svg width="22" height="20" viewBox="0 0 22 20"><rect x="2" y="3" width="18" height="14" fill="none" stroke="#222" stroke-width="2"/><path d="M5 8h12M5 12h12" stroke="#222" stroke-width="2"/></svg>SERVICES</div>
    <div class="nav-item" style="left:530px">
      <svg width="22" height="20" viewBox="0 0 22 20"><rect x="2" y="3" width="18" height="14" fill="none" stroke="#222" stroke-width="2"/><path d="M4 15l5-6 4 4 3-3 3 5z" fill="#222"/></svg>DEVELOPMENT</div>
    <div class="nav-item" style="left:688px">
      <svg width="22" height="20" viewBox="0 0 22 20"><rect x="2" y="4" width="18" height="13" fill="none" stroke="#222" stroke-width="2"/><path d="M11 7v7" stroke="#222" stroke-width="2"/></svg>JOB POST</div>
    <div class="nav-item" style="left:835px">
      <svg width="22" height="20" viewBox="0 0 22 20"><path d="M2 3h18v11H9l-4 4v-4H2z" fill="none" stroke="#222" stroke-width="2"/><path d="M6 9h2M10 9h2M14 9h2" stroke="#222" stroke-width="2"/></svg>CONTACT</div>
  </nav>
  <h1 class="hero-title">Software Development Consulting Company</h1>
  <p class="hero-lead">It is a long established fact that a reader will be distracted by the readable content of a page when looking at its layout. The point of using Lorem Ipsum</p>
  <div class="hero-down">
    <svg width="30" height="20" viewBox="0 0 30 20"><path d="M3 3l12 14L27 3" fill="none" stroke="#fff" stroke-width="2.5"/></svg>
  </div>
</section>

<div class="plus-box" style="left:958px;top:787px;width:76px;height:95px;z-index:2">
  <svg width="18" height="22" viewBox="0 0 18 22"><path d="M9 21V2M2 9l7-7 7 7" fill="none" stroke="#fff" stroke-width="2"/></svg>
</div>
<div class="plus-box" style="left:1036px;top:787px;width:75px;height:95px;z-index:2">
  <svg width="24" height="24" viewBox="0 0 24 24"><path d="M12 2v20M2 12h20" stroke="#fff" stroke-width="2"/></svg>
</div>

<section class="section services">
  <h2 class="section-title" style="top:96px">Services</h2>
  <p class="section-sub" style="top:141px">Check Our Latest Work</p>

  <article class="card active" style="left:118px">
    <div class="card-icon">
      <svg width="34" height="26" viewBox="0 0 34 26"><rect x="6" y="3" width="22" height="15" fill="none" stroke="#222" stroke-width="2.5"/><path d="M2 22h30" stroke="#222" stroke-width="3"/></svg>
    </div>
    <h3>SOFTWARE DEVELOPMENT</h3>
    <p>It is a long established fact that a reader will be distracted by the readable content of a page when looking at its layout. The point of using Lorem Ipsum is that it has a more-or-less normal distribution of letters, as</p>
    <span class="more">Read More</span>
  </article>

  <article class="card" style="left:441px">
    <div class="card-icon">
      <svg width="28" height="28" viewBox="0 0 28 28" fill="#fff"><circle cx="14" cy="4" r="2.4"/><circle cx="21" cy="7" r="2.2"/><circle cx="24" cy="14" r="2"/><circle cx="21" cy="21" r="1.8"/><circle cx="14" cy="24" r="1.6"/><circle cx="7" cy="21" r="1.5"/><circle cx="4" cy="14" r="1.4"/><circle cx="7" cy="7" r="1.3"/></svg>
    </div>
    <h3>TECHNOLOGY</h3>
    <p>It is a long established fact that a reader will be distracted by the readable content of a page when looking at its layout. The point of using Lorem Ipsum is that it has a more-or-less normal distribution of letters, as</p>
    <span class="more">Read More</span>
  </article>

  <article class="card" style="left:765px">
    <div class="card-icon">
      <svg width="28" height="28" viewBox="0 0 28 28"><path d="M25 3L3 13l10 2 2 10z" fill="#fff"/></svg>
    </div>
    <h3>JOB POST</h3>
    <p>It is a long established fact that a reader will be distracted by the readable content of a page when looking at its layout. The point of using Lorem Ipsum is that it has a more-or-less normal distribution of letters, as</p>
    <span class="more">Read More</span>
  </article>
</section>

<section class="section about">
  <h2 class="section-title" style="top:86px">About Us</h2>
  <div class="about-photo" role="img" aria-label="Photo of a business team seated around a meeting table with laptops"></div>
  <p class="about-text">It is a long established fact that a reader will be distracted by the readable content of a page when looking at its layout. The point of using Lorem Ipsum is that it has a more-or-less normal distribution of letters, as opposed to using 'Content here, content here', making it look like readable English. Many desktop publishing packages and web page editors now use Lorem Ipsum as their default model text, and a search for 'lorem ipsum' will uncover many web sites still in their infancy. Various versions have evolved over the years, sometimes by accident, sometimes on purpose (injected humour and the like).</p>
  <span class="about-more">Read More</span>
</section>

<section class="section contact">
  <h2 class="section-title" style="top:53px">Contact Us</h2>

  <div class="info-row" style="top:136px">
    <span class="ico"><svg width="18" height="16" viewBox="0 0 18 16"><path d="M9 1L1 8h2v7h4v-4h4v4h4V8h2z" fill="#8a8a8a"/></svg></span>
    <span>Level 4, 18 Harbor Lane<br>Lorem Ipsum, VIC 3104<br>Dolar sit</span>
  </div>
  <div class="info-row" style="top:218px">
    <span class="ico"><svg width="18" height="18" viewBox="0 0 18 18"><path d="M4 1l3 4-2 2c1 3 3 5 6 6l2-2 4 3-2 3C8 17 1 10 1 3z" fill="#8a8a8a"/></svg></span>
    <span>+2541 230 774</span>
  </div>
  <div class="info-row web" style="top:263px">
    <span class="ico"><svg width="30" height="16" viewBox="0 0 30 16"><rect x="10" y="2" width="19" height="13" fill="none" stroke="#8a8a8a" stroke-width="1.5"/><path d="M10 2l9.5 7L29 2M1 6h6M3 10h5" fill="none" stroke="#8a8a8a" stroke-width="1.5"/></svg></span>
    <span>www.norvaleconsult.com</span>
  </div>

  <div class="field" style="left:437px;top:139px;width:282px;height:40px">Name*</div>
  <div class="field" style="left:437px;top:189px;width:282px;height:40px">Email Address*</div>
  <div class="field" style="left:437px;top:238px;width:282px;height:40px">Subject*</div>
  <div class="field" style="left:730px;top:139px;width:304px;height:137px">Message*</div>
  <div class="send-btn">Send Message</div>

  <div class="newsletter">
    <h4>Subscribe to Our Newsletter</h4>
    <p>Subscribe to new Products, Services and Stuff</p>
    <div class="news-input">
      <svg width="18" height="12" viewBox="0 0 18 12"><rect x="1" y="1" width="16" height="10" fill="none" stroke="#333" stroke-width="1.4"/><path d="M1 1l8 6 8-6" fill="none" stroke="#333" stroke-width="1.4"/></svg>
      Email Address
    </div>
    <div class="news-go">GO</div>
  </div>

  <div class="map" role="img" aria-label="Street map showing the office location with a pin marker"></div>
</section>

<footer class="site-footer">
  <div class="footer-social"><span></span><span></span><span></span><span></span><span></span></div>
  <p class="footer-links">Terms &amp; Condition<i>|</i>Privacy Policy<i>|</i>Site Map</p>
  <div class="footer-up">
    <svg width="16" height="10" viewBox="0 0 16 10"><path d="M2 8l6-6 6 6" fill="none" stroke="#eee" stroke-width="2"/></svg>
  </div>
</footer>

</body>
</html>
```